Website redesign for a national printing company

Our current website is dated and boring: tidewellflags.com

We are looking for a fresh, modern design. We need a clean, minimal design that is also elegant, really shows off large, bright photos of our banners in action and POPS. Our goal is to showcase our beautiful banners, while also giving the user the confidence in our company that we will provide friendly, fast service, fast printing, and deliver their banners on time for their event.

I want a nice flow to the website, the design should tie in well with the printing feel. Here is an example of clean, beautiful design that ties in to the industry - https://www.vorpa.com/ - notice how the buttons are like chat icons, for example.

More examples:

Nice clean design https://www.brimlet.com/

https://quelmoor.com/ nice and clean, but it POPS really well.

I like https://www.fendrawick.com/

https://www.pruvel.com/ gorgeous site, clean, modern

Beautiful, simple, clean, modern - https://tanvirepay.com/en-us/

These websites are not from the print industry, that’s because most printers don’t have good websites - they are more focused on local businesses, referrals, not really online marketing.

But keep in mind in your design that we need to give the feel that we are printing their banners beautifully, fast, with great service.

https://www.gleamvoxa.com/ so clean, bold, clear to the user what the company does. Love this simple yet elegant design.

https://www.k7.com/ - so pretty! And still so simple and obvious to the user what to do on their site.

https://zelvin.com/

https://marrowfinch.com/us/en/ big and bold - yet super nicely designed with so many nice touches

https://postwrenly.com/ - also clean, simple, and so obvious to the user to take action and contact the company
Updates

I just updated the job brief, and you can also view it in full here - https://files.qorvanet.com/document/d/8Hpz3LRQx-41mTb92nWvJcOaEs-Y67kd0Gf57JuXRTNe/edit?usp=sharing

Target Market(s)

Please read this customer persona - https://files.qorvanet.com/document/d/8Hpz3LRQx-41mTb92nWvJcOaEs-Y67kd0Gf57JuXRTNe/edit?usp=sharing

Industry/Entity Type

Printing

Number of Pages Required

1 page

Requirements
Must have
• Nice flow to the website, the design should tie in well with the printing feel. Here is an example of clean, beautiful design that ties in to the industry - https://www.vorpa.com/ - notice how the buttons are like chat icons, for example.
Should not have
• No filters on the images, we want large, beautiful images.

```html
<!DOCTYPE html>
<html lang="en">
<head>
<meta charset="utf-8">
<title>Tidewell Flags — Custom Banner Printing</title>
<link href="https://fonts.googleapis.com/css2?family=Poppins:wght@300;400;500;600;700;800&display=swap" rel="stylesheet">
<style>
:root{
  --blue:#1c3ba8;
  --blue-dark:#16308c;
  --navy:#24346f;
  --ink:#1d1d1f;
  --text:#3a3a3a;
  --muted:#f0f1f4;
  --line:#9a9a9a;
  --white:#ffffff;
}
*{margin:0;padding:0;box-sizing:border-box}
html,body{width:1200px;height:4630px;overflow:hidden}
body{position:relative;font-family:'Poppins',sans-serif;color:var(--text);background:var(--white)}
.abs{position:absolute}
.btn{position:absolute;display:flex;align-items:center;justify-content:center;background:var(--blue);color:var(--white);font-weight:600;font-size:13px;letter-spacing:.3px;border-radius:4px 4px 4px 0;text-transform:uppercase}
.btn::after{content:"";position:absolute;left:0;bottom:-8px;border-top:8px solid var(--blue);border-right:10px solid transparent}
.section-title{position:absolute;font-size:38px;font-weight:500;color:var(--ink);text-transform:uppercase;letter-spacing:.5px}
.section-title b{color:var(--blue);font-weight:800}

/* header */
.site-header{left:0;top:0;width:1200px;height:84px;background:var(--white);z-index:5}
.brand{left:95px;top:18px;text-align:center;width:210px}
.brand-name{font-size:32px;font-weight:600;color:var(--ink);line-height:1;letter-spacing:-.5px}
.brand-sub{font-size:12px;letter-spacing:9px;color:var(--ink);margin-top:4px}
.nav a{position:absolute;top:36px;font-size:13px;font-weight:500;color:var(--ink);text-decoration:none}
.nav a.active{color:var(--blue)}

/* hero */
.hero{left:0;top:84px;width:1200px;height:680px;background:linear-gradient(180deg,#2f3f7e 0%,#27346a 45%,#1d2756 80%,#39415f 100%)}
.hero-title{left:0;top:290px;width:1200px;text-align:center;font-size:58px;font-weight:700;color:var(--white);letter-spacing:1px}
.hero-sub{left:0;top:368px;width:1200px;text-align:center;font-size:27px;color:var(--white);line-height:44px}
.dots{left:536px;top:673px;display:flex;gap:10px;align-items:center}
.dots span{width:6px;height:6px;border-radius:50%;background:var(--white)}
.dots span.on{width:12px;height:12px}

/* about */
.about-photo{left:86px;top:850px;width:420px;height:420px;border-radius:50%;background:linear-gradient(135deg,#d9d4cd 0%,#a9a6a4 45%,#5f3a34 100%)}
.about-title{left:584px;top:830px}
.about p,.about h4{position:absolute;left:585px;width:450px;font-size:16px;line-height:26px;color:var(--text)}
.about h4{font-weight:600;color:var(--ink)}

/* testimonials */
.testimonials{left:0;top:1356px;width:1200px;height:652px;background:var(--muted)}
.t-card{position:absolute;background:var(--white);box-shadow:0 6px 18px rgba(0,0,0,.08)}
.t-quote{position:absolute;left:26px;top:20px}
.t-name{position:absolute;left:78px;top:40px;font-size:23px;font-weight:500;color:var(--blue)}
.t-say{position:absolute;left:78px;top:68px;font-size:29px;font-weight:700;color:var(--ink)}
.t-body{position:absolute;left:32px;top:120px;width:320px;font-size:15px;line-height:26px;color:var(--text)}
.arrow-btn{position:absolute;width:58px;height:58px;border-radius:50%;background:var(--white);box-shadow:0 4px 12px rgba(0,0,0,.12);display:flex;align-items:center;justify-content:center}

/* gallery */
.tab{position:absolute;top:2173px;border-top:2px solid var(--line);padding-top:12px;font-size:14px;font-weight:500;color:var(--ink);line-height:23px;text-transform:uppercase}
.tab.active{border-color:var(--blue)}
.g-cell{position:absolute}

/* process */
.process{left:0;top:2830px;width:1200px;height:453px;background:var(--muted)}
.step{position:absolute;text-align:center;color:var(--blue)}
.step .lab{font-size:26px;font-weight:600}
.step .num{font-size:48px;font-weight:600;line-height:58px}
.step .txt{font-size:18px;line-height:22px}

/* quote */
.quote-text{left:120px;top:3430px;width:545px;font-size:16px;line-height:28px;color:var(--ink)}

/* how */
.how-band{left:0;top:3610px;width:1200px;height:450px;background:var(--muted)}
.how-frame{left:393px;top:3651px;width:715px;height:474px;border:2px solid var(--blue)}
.how-photo{left:426px;top:3590px;width:714px;height:508px;background:linear-gradient(160deg,#3a4a8c 0%,#23337a 50%,#1a2762 100%)}
.how-box{left:63px;top:3678px;width:400px;height:331px;background:var(--white);box-shadow:0 6px 20px rgba(0,0,0,.08)}

/* why */
.why-card{position:absolute;top:4251px;width:211px;height:194px;background:var(--white);box-shadow:0 6px 20px rgba(0,0,0,.1);text-align:center}
.why-card svg{margin-top:48px}
.why-card p{font-size:15px;color:var(--ink);margin-top:22px}

.site-footer{left:0;top:4535px;width:1200px;height:95px;background:var(--blue);color:var(--white);font-size:17px;display:flex;align-items:center;justify-content:center}
</style>
</head>
<body>

<header class="site-header abs">
  <div class="brand abs">
    <div class="brand-name">Tidewell</div>
    <div class="brand-sub">FLAGS</div>
  </div>
  <nav class="nav">
    <a class="active" style="left:411px">HOME</a>
    <a style="left:483px">ABOUT</a>
    <a style="left:566px">SERVICES</a>
    <a style="left:668px">TESTIMONIALS</a>
    <a style="left:801px">CONTACT US</a>
  </nav>
  <div class="btn" style="left:946px;top:30px;width:121px;height:33px;font-size:12px">Get a quote</div>
</header>

<section class="hero abs" role="img" aria-label="Large blue printed banner wrapped around a stage platform"></section>
<h1 class="hero-title abs">TIDEWELL FLAGS</h1>
<p class="hero-sub abs">Making Brands Look Good On Stage For<br>Over Two Decades</p>
<div class="btn" style="left:503px;top:480px;width:140px;height:36px">Get a quote</div>
<div class="dots abs"><span></span><span></span><span class="on"></span><span></span><span></span></div>
<svg class="abs" style="left:0;top:680px" width="1200" height="90" viewBox="0 0 1200 90">
  <path d="M0 30 C200 90 400 70 600 40 C800 10 1000 10 1200 40 L1200 90 L0 90Z" fill="#1c3ba8"/>
  <path d="M0 36 C200 96 400 78 600 50 C800 22 1000 24 1200 56 L1200 90 L0 90Z" fill="#fff"/>
</svg>

<section class="about">
  <svg class="abs" style="left:70px;top:835px" width="450" height="450" viewBox="0 0 450 450">
    <path d="M225 10 A215 215 0 1 0 440 225" fill="none" stroke="#1c3ba8" stroke-width="6"/>
    <path d="M380 70 A215 215 0 0 1 440 225" fill="none" stroke="#1c3ba8" stroke-width="3"/>
  </svg>
  <div class="about-photo abs" role="img" aria-label="Print technician reviewing a freshly printed sheet beside a large format printer"></div>
  <h2 class="section-title about-title"><b>About</b> us</h2>
  <p style="top:893px">For over two decades, Tidewell Flags has been the go-to source for high-quality custom printing for large format banners, plastic roll banners, stage backdrops and mobile stage festival banners.</p>
  <h4 style="top:1026px">It's Your Turn To Meet The Friendliest Printers In The Business :</h4>
  <p style="top:1084px">We would love to get your banners rolling - get in touch with us today and you'll have a trusted, communicative team member talking with you within one business day to help you get your order going.</p>
  <div class="btn" style="left:587px;top:1209px;width:140px;height:36px">About us</div>
</section>

<section class="testimonials abs"></section>
<h2 class="section-title" style="left:0;width:1200px;text-align:center;top:1392px"><b>Client</b> testimonials</h2>
<div class="t-card" style="left:-20px;top:1478px;width:45px;height:437px"></div>

<article class="t-card" style="left:54px;top:1478px;width:372px;height:437px">
  <svg class="t-quote" width="72" height="80" viewBox="0 0 72 80"><path d="M0 20 Q0 0 20 0 L30 0 L30 80 L0 80Z M36 20 Q36 0 56 0 L66 0 L66 80 L36 80Z" fill="#e2e3e6"/></svg>
  <div class="t-name">Marlon Vesk</div>
  <div class="t-say">CLIENT SAY</div>
  <p class="t-body">Dana and the team at Tidewell Flags have been great to work with. Their eye to detail is spot on. Don't be afraid to ask as many questions as you like. Fast shipping and wonderful quality product. Will be using them again soon. Thank you from Fernhollow County, North America's #1. Copper Valley Revival Tribute Show. CVR.</p>
  <div class="btn" style="left:36px;top:362px;width:112px;height:36px;font-size:12px">Read more</div>
</article>

<article class="t-card" style="left:449px;top:1478px;width:372px;height:406px">
  <svg class="t-quote" width="72" height="80" viewBox="0 0 72 80"><path d="M0 20 Q0 0 20 0 L30 0 L30 80 L0 80Z M36 20 Q36 0 56 0 L66 0 L66 80 L36 80Z" fill="#e2e3e6"/></svg>
  <div class="t-name">Orla Pennick</div>
  <div class="t-say">CLIENT SAY</div>
  <p class="t-body">We have ordered a variety of blow through stage banners and other vinyl banners and the ordering process has been extremely efficient, accurate, and the customer service top notch. The products themselves arrive quickly and are great quality. We highly recommend!</p>
  <div class="btn" style="left:36px;top:332px;width:112px;height:36px;font-size:12px">Read more</div>
</article>

<article class="t-card" style="left:844px;top:1478px;width:380px;height:309px">
  <svg class="t-quote" width="72" height="80" viewBox="0 0 72 80"><path d="M0 20 Q0 0 20 0 L30 0 L30 80 L0 80Z M36 20 Q36 0 56 0 L66 0 L66 80 L36 80Z" fill="#e2e3e6"/></svg>
  <div class="t-name">Janine Corbell</div>
  <div class="t-say">CLIENT SAY</div>
  <p class="t-body">Mara was extremely helpful and knowledgeable. Great quality, quick turn around. I would highly recommend this company.</p>
  <div class="btn" style="left:32px;top:234px;width:112px;height:36px;font-size:12px">Read more</div>
</article>

<div class="arrow-btn" style="left:970px;top:1914px"><svg width="24" height="24" viewBox="0 0 24 24"><path d="M20 12H5M11 6l-6 6 6 6" fill="none" stroke="#1d1d1f" stroke-width="2.2"/></svg></div>
<div class="arrow-btn" style="left:1056px;top:1914px"><svg width="24" height="24" viewBox="0 0 24 24"><path d="M4 12h15M13 6l6 6-6 6" fill="none" stroke="#1d1d1f" stroke-width="2.2"/></svg></div>

<section class="gallery">
  <h2 class="section-title" style="left:0;width:1200px;text-align:center;top:2072px"><b>Our</b> gallery</h2>
  <div class="tab" style="left:135px;width:176px">Plastic roll banners</div>
  <div class="tab active" style="left:377px;width:180px">Festival banners and stage backdrops</div>
  <div class="tab" style="left:625px;width:207px">Large format and mesh banners</div>
  <div class="tab" style="left:875px;width:131px">Cloth banners</div>

  <div class="g-cell" style="left:95px;top:2267px;width:300px;height:238px;background:linear-gradient(180deg,#8fb0d8 0%,#c9a24a 45%,#5a4330 100%)" role="img" aria-label="Outdoor festival stage with a printed banner header above a crowd"></div>
  <div class="g-cell" style="left:95px;top:2517px;width:300px;height:238px;background:linear-gradient(180deg,#5e78c8 0%,#c89ab8 45%,#5e7a40 100%)" role="img" aria-label="Mobile stage with printed side banners at dusk on a lawn"></div>
  <div class="g-cell" style="left:406px;top:2267px;width:330px;height:488px;background:linear-gradient(180deg,#3b3a44 0%,#2b2c3a 50%,#4a3a36 100%)" role="img" aria-label="Indoor concert stage with a large printed backdrop">
    <svg class="abs" style="left:152px;top:308px" width="26" height="26" viewBox="0 0 26 26"><circle cx="13" cy="13" r="12" fill="#1c3ba8"/><circle cx="12" cy="12" r="4.5" fill="none" stroke="#fff" stroke-width="1.6"/><path d="M15.5 15.5l3.5 3.5" stroke="#fff" stroke-width="1.6"/></svg>
    <div class="abs" style="left:0;top:356px;width:330px;text-align:center;color:#fff;font-size:19px">VIEW MORE</div>
    <div class="abs" style="left:0;top:390px;width:330px;text-align:center;color:#fff;font-size:15px;line-height:25px">FESTIVAL BANNERS AND<br>STAGE BACKDROPS</div>
  </div>
  <div class="g-cell" style="left:749px;top:2267px;width:298px;height:238px;background:linear-gradient(180deg,#4a6aa8 0%,#e08a3a 50%,#3a2a28 100%)" role="img" aria-label="Night festival stage with flames and printed banners"></div>
  <div class="g-cell" style="left:749px;top:2517px;width:298px;height:238px;background:linear-gradient(180deg,#dfe4ea 0%,#6b8ab8 50%,#3a5680 100%)" role="img" aria-label="Outdoor arts stage with printed celebration banners"></div>
</section>

<section class="process abs"></section>
<h2 class="section-title" style="left:0;width:1200px;text-align:center;top:2866px;font-size:36px"><b>Process</b> of getting banners printed</h2>
<svg class="abs" style="left:0;top:2940px" width="1200" height="290" viewBox="0 0 1200 290">
  <polygon points="100,30 244,30 297,138 244,246 100,246 47,138" fill="none" stroke="#1c3ba8" stroke-width="3"/>
  <polygon points="354,30 498,30 551,138 498,246 354,246 301,138" fill="none" stroke="#1c3ba8" stroke-width="3"/>
  <polygon points="620,2 796,2 857,137 796,272 620,272 559,137" fill="#1c3ba8"/>
  <polygon points="918,30 1062,30 1115,138 1062,246 918,246 865,138" fill="none" stroke="#1c3ba8" stroke-width="3"/>
</svg>
<div class="step" style="left:72px;top:2995px;width:200px"><div class="lab">Step</div><div class="num">1</div><div class="txt">Lorem Ipsum is simply dummy</div></div>
<div class="step" style="left:326px;top:2995px;width:200px"><div class="lab">Step</div><div class="num">2</div><div class="txt">Lorem Ipsum is simply dummy</div></div>
<div class="step" style="left:598px;top:2963px;width:220px;color:#fff"><div class="lab">Step</div><div class="num">3</div><div class="txt" style="font-size:16px">Lorem Ipsum is simply dummy text of the printing and typesetting industry. Lorem Ipsum has been the industry's standard</div></div>
<div class="step" style="left:890px;top:2995px;width:200px"><div class="lab">Step</div><div class="num">4</div><div class="txt">Lorem Ipsum is simply dummy</div></div>

<section class="quote">
  <h2 class="section-title" style="left:117px;top:3358px"><b>Get</b> a quote</h2>
  <p class="quote-text abs">Lorem ipsum dolor sit amet, consectetur adipiscing elit, sed do eiusmod tempor incididunt ut labore et dolore magna aliqua. Quis ipsum suspendisse ultrices gravida. Risus commodo viverra maecenas accumsan lacus vel facilisis.</p>
  <svg class="abs" style="left:620px;top:3360px" width="132" height="40" viewBox="0 0 132 40"><path d="M3 34 Q60 16 124 20" fill="none" stroke="#1c3ba8" stroke-width="3"/><path d="M106 6 L126 20 L108 34" fill="none" stroke="#1c3ba8" stroke-width="3"/></svg>
  <div class="btn" style="left:738px;top:3421px;width:279px;height:68px;font-size:25px;font-weight:600">Get a quote now</div>
</section>

<section class="how">
  <div class="how-band abs"></div>
  <div class="how-frame abs"></div>
  <div class="how-photo abs" role="img" aria-label="Blue printed mesh banner wrapped around a two-level event hospitality structure"></div>
  <div class="how-box abs">
    <h2 class="section-title" style="left:19px;top:52px"><b>How</b> we work</h2>
    <p class="abs" style="left:19px;top:112px;width:360px;font-size:15px;line-height:28px;color:var(--ink)">Lorem ipsum dolor sit amet, consectetur adipiscing elit, sed do eiusmod tempor incididunt ut labore et dolore magna aliqua. Quis ipsum suspendisse ultrices gravida. Risus commodo viverra maecenas accumsan lacus vel facilisis.</p>
  </div>
</section>

<section class="why">
  <h2 class="section-title" style="left:72px;top:4262px"><b>Why</b> choose us</h2>
  <p class="abs" style="left:76px;top:4320px;width:340px;font-size:15px;line-height:26px;color:var(--ink)">Lorem Ipsum is simply dummy text of the printing and typesetting industry. Lorem Ipsum has been the industry's standard dummy text ever since the 1500s, when an unknown printer</p>
  <div class="why-card" style="left:445px">
    <svg width="80" height="70" viewBox="0 0 80 70"><circle cx="40" cy="12" r="9" fill="none" stroke="#111" stroke-width="3"/><path d="M6 30 L30 30 L46 44 L40 52 L26 42 M74 30 L50 30 L34 46 L40 54 L56 40 M6 30 L6 48 L22 58 M74 30 L74 48 L58 58" fill="none" stroke="#111" stroke-width="4" stroke-linejoin="round"/></svg>
    <p>Friendly</p>
  </div>
  <div class="why-card" style="left:673px">
    <svg width="80" height="70" viewBox="0 0 80 70"><circle cx="46" cy="38" r="24" fill="none" stroke="#111" stroke-width="4"/><path d="M40 8h12M46 8v6M46 26v12l8 6M4 30h14M8 40h10M4 50h14" fill="none" stroke="#111" stroke-width="4"/></svg>
    <p>Fast Service</p>
  </div>
  <div class="why-card" style="left:900px">
    <svg width="80" height="70" viewBox="0 0 80 70"><rect x="18" y="6" width="44" height="16" fill="none" stroke="#111" stroke-width="4"/><rect x="8" y="22" width="64" height="28" rx="4" fill="none" stroke="#111" stroke-width="4"/><rect x="20" y="40" width="40" height="24" fill="#fff" stroke="#111" stroke-width="4"/><path d="M28 50h24M28 57h16" stroke="#111" stroke-width="3"/></svg>
    <p>fast Printing</p>
  </div>
</section>

<footer class="site-footer abs">Copyright © Tidewell Flags 2023. All rights reserved.</footer>

</body>
</html>
```